PantryLoop.com Brochure - Please visit my creative directory

Grocery Delivery Service covering Detroit Area needs a brochure and print material. Our web site is 98% ready and usable for your layout.

The web site is PantryLoop.com
You must include elements from my creative library at
http://www.brennaltovik.com/PantryLoopCreative/

My competitors are http://www.basketrungreens.com/ and
https://www.cartlane.com/detroit-grocery-delivery/?gclid=XPlwta7K3R2QBMLdZnweTr5V8B

Use a medium-low amount of text, lots of highlights and action visuals

Use my web site pages to for FAQ info.
Just so this box will fill up I'll dump some of my web site code here.

PantryLoop.com enhancing your lifestyle
Saving you time, better choices, and doing the physical work for you. That’s the PantryLoop.com lifestyle.

Saving you time - Add up all the time you spend doing your grocery shopping. Now try doing that chore in 15 minutes. Our long standing customers use previous shopping lists to quickly re-order new items while adding a few sale, new, and seasonal selections. Like any new store you walk into your first shopping session will take more time as you explore all we have to offer.
Better choices – Search for organic or low-salt items. Always know your total price in-cart so you don’t bust your budget. No impulse candy at checkout or tricky cross-selling add-ons.
Physical work – We bring this right to your door and help you unload. We fight the traffic, navigate the store, even 8th floor of your office building. Heavy stuff, no problem.

PantryLoop.com rely on us

Schedule your delivery by appointment as soon as tomorrow.
Items you order are bar code scanned for exact matches. Any substitution is accurately recorded and displayed on the receipt at delivery.
Have an event in Detroit Area, rely on us to provide.
Our climate controlled vehicles get frozen ice cream in your freezer.
Office break rooms filled up with high quality energy for your workforce.

PantryLoop.com service to support the New Detroit Lifestyle

Incredible communities are forming across the resurgent Detroit Area. The challenge of accessible grocery choices is now solved with PantryLoop.com. No long walks, bicycle trips, elevators, or parking tickets with only a hand full of groceries.
Use that time you save to explore the Vellmark Trail, stay out late in Pell Yard, more time cooking (not shopping) with family & friends.

Target Market(s)

City of Detroit and surrounding suburbs.
Out of town guests and event holders.
Residential families
Assisted living elderly
Business employee break rooms
People with disabilities
People with injuries
People without cars
People that hate grocery shopping

Industry/Entity Type

Delivery Service

Font styles to use
Other font styles liked:
• something like my logo, but a little more generic, dark, and readable

Colors
ec1f27
9bcb3c
b1b1b1

Requirements
Must have
• my logo in regular and circle.
• A color palette that matches the logo. Soft base colors with vivid enhancements
• Any where PantryLoop.com is mentioned the F and H must be capital.
Nice to have
• Theme as
• 1. How it works for half of information. (Use web site, pick delivery time, pay, and then delivery is executed)
• 2. Who will use this service
• 3. How will this service enhance your lifestyle.
Should not have
• I want you to use provided photos where possible, stay away from generic stock photography. You can use a little stock photography for food, but don't only show produce.

```html
<!DOCTYPE html>
<html lang="en">
<head>
<meta charset="utf-8">
<title>PantryLoop.com – Enhancing your lifestyle</title>
<link rel="stylesheet" href="https://fonts.googleapis.com/css2?family=Caveat:wght@400;500&family=Arimo:wght@700&display=swap">
<style>
  :root {
    --paper: #edebe7;
    --ink: #807c78;
    --heading: #8c8782;
    --coral: #f0673f;
    --coral-soft: #f59a80;
    --teal: #80c6c1;
  }
  * { margin: 0; padding: 0; box-sizing: border-box; }
  html, body { width: 1200px; height: 927px; overflow: hidden; background: var(--paper); }
  .panel { position: relative; width: 1200px; height: 927px; background: var(--paper); overflow: hidden; }

  .section-title {
    position: absolute;
    font-family: "Caveat", cursive;
    font-weight: 400;
    font-size: 56px;
    color: var(--heading);
    letter-spacing: 1px;
    line-height: 1;
  }
  .copy {
    position: absolute;
    font-family: "Arimo", Arial, sans-serif;
    font-weight: 700;
    font-size: 20px;
    line-height: 25.5px;
    color: var(--ink);
    text-align: center;
  }
  .copy p + p { margin-top: 25px; }
  .copy .right { display: block; text-align: right; }

  .photo {
    position: absolute;
    border-radius: 50%;
    border-style: solid;
  }
  .photo--coral { border-color: var(--coral); }
  .photo--teal { border-color: var(--teal); }

  .photo--pasta { left: 444px; top: 53px; width: 258px; height: 258px; border-width: 7px;
    background: radial-gradient(circle at 50% 45%, #d9a86a 0%, #b77a45 35%, #4a4642 70%, #2f2d2c 100%); }
  .photo--grapes { left: 568px; top: 242px; width: 190px; height: 190px; border-width: 8px;
    background: radial-gradient(circle at 45% 40%, #3a3f5c 0%, #23263b 45%, #b89a86 80%, #d9d2c8 100%); }
  .photo--delivery { left: 848px; top: 296px; width: 290px; height: 290px; border-width: 9px;
    background: linear-gradient(180deg, #a9c4e0 0%, #c9d6de 35%, #f2f2f2 55%, #5a5a5a 85%, #3a3a3a 100%); }
  .photo--unloading { left: -64px; top: 528px; width: 430px; height: 430px; border-width: 11px;
    background: linear-gradient(160deg, #6f8f4a 0%, #d8dde2 35%, #f4f4f4 55%, #8b8b8b 85%, #5b5b5b 100%); }

  .dot { position: absolute; border-radius: 50%; }
  .dot--large { left: 901px; top: 765px; width: 152px; height: 152px; background: var(--coral); }
  .dot--small { left: 974px; top: 732px; width: 112px; height: 112px; background: var(--coral-soft); }
</style>
</head>
<body>
<main class="panel">

  <h2 class="section-title" style="left:22px; top:74px;">Saving you time-</h2>
  <div class="copy" style="left:30px; top:147px; width:340px;">
    <p>Add up all the time you spend<br>doing your grocery shopping.<br>Now try doing that chore in 15<br>minutes.</p>
    <p>Our long standing customers<br>use previous shopping lists<br>to quickly reorder new items<br>while adding a few sale, new,<br>and seasonal selections.<br>Like any new store you walk<br>into your first shopping<br>session will take more time as<br><span class="right">you explore all&nbsp;&nbsp;&nbsp;&nbsp;</span><span class="right">we have&nbsp;&nbsp;</span><span class="right" style="margin-right:-2px;">to offer.</span></p>
  </div>

  <div class="photo photo--coral photo--pasta" role="img" aria-label="Plate of spaghetti with chicken and herbs"></div>
  <div class="photo photo--teal photo--grapes" role="img" aria-label="Hands holding a bunch of dark grapes"></div>

  <h2 class="section-title" style="left:415px; top:487px;">Better choices-</h2>
  <div class="copy" style="left:440px; top:546px; width:320px;">
    <p>Search for organic or low<br>salt items.<br>Always know your total<br>price in-cart so you don’t<br>bust your budget.</p>
    <p>No impulse candy at<br>checkout or tricky<br>cross-selling add-ons.</p>
  </div>

  <h2 class="section-title" style="left:812px; top:76px;">Phsyical work-</h2>
  <div class="copy" style="left:815px; top:141px; width:370px;">
    <p>We bring this right to your door<br>and help you unload.<br>We fight the traffic, navigate the<br>store, and even deliver to the 8th<br>floor of your office building.</p>
  </div>

  <div class="photo photo--teal photo--delivery" role="img" aria-label="Delivery driver wheeling groceries from a white van"></div>

  <div class="copy" style="left:845px; top:685px; width:300px;">
    <p>Heavy stuff? No problem.</p>
  </div>

  <div class="photo photo--coral photo--unloading" role="img" aria-label="Driver unloading a basket of groceries from a delivery van"></div>

  <div class="dot dot--large" aria-hidden="true"></div>
  <div class="dot dot--small" aria-hidden="true"></div>

</main>
</body>
</html>
```